Boat business cards

I'm looking for business cards with the two logos I've attached. I don't have an specific idea in mind and open to anything. All the usual info will be on the card. Name, position in company, nr, email, address, ect. The company rents out these two boats for charters and fishing.

```html
<!DOCTYPE html>
<html lang="en">
<head>
<meta charset="utf-8">
<title>Polar Tide Business Cards</title>
<link rel="stylesheet" href="https://fonts.googleapis.com/css2?family=Poppins:wght@400;500;600;700&display=swap">
<style>
  :root {
    --backdrop: #8d8d8d;
    --card-front: #9bb5d6;
    --card-back: #e7e7ea;
    --ink: #141414;
    --ink-soft: #2a2a2a;
    --bronze: #8b7052;
    --steel: #5a5d63;
    --hull-blue: #6f93c2;
  }
  * { box-sizing: border-box; margin: 0; padding: 0; }
  html, body { width: 1200px; height: 1101px; overflow: hidden; }
  body {
    background: var(--backdrop);
    font-family: "Poppins", sans-serif;
    position: relative;
  }
  .card { position: absolute; width: 302px; height: 529px; overflow: hidden; }
  .card-front { left: 246px; top: 268px; background: var(--card-front); }
  .card-back { left: 641px; top: 267px; background: var(--card-back); }

  .yacht-art {
    position: absolute; left: 52px; top: 78px; width: 200px; height: 50px;
    background: linear-gradient(180deg, #eef0f2 0%, #d6d9dc 35%, #8c6a45 60%, #6b5033 80%, #7e9cc8 100%);
    border-radius: 4px 30px 6px 6px;
  }
  .brand-name {
    position: absolute; left: 0; right: 0; top: 132px;
    text-align: center; font-weight: 600; font-size: 22px; color: var(--ink);
    letter-spacing: 1px;
  }
  .person-name {
    position: absolute; left: 33px; top: 254px;
    font-weight: 600; font-size: 20px; line-height: 25px; letter-spacing: 1.6px; color: var(--ink);
  }
  .rule { position: absolute; left: 33px; width: 232px; height: 2px; background: var(--ink-soft); }
  .rule-top { top: 314px; }
  .rule-bottom { top: 423px; }
  .job-title {
    position: absolute; left: 33px; top: 325px;
    font-weight: 500; font-size: 13.5px; letter-spacing: 0.4px; color: var(--ink);
  }
  .contact-icons { position: absolute; left: 37px; top: 386px; display: flex; gap: 13px; }
  .contact-icons svg { width: 25px; height: 25px; display: block; }
  .contact-list {
    position: absolute; left: 33px; top: 439px; list-style: none;
    font-weight: 500; font-size: 13.5px; line-height: 18px; letter-spacing: 0.3px; color: var(--ink);
  }

  .boat-art {
    position: absolute; left: 40px; top: 72px; width: 180px; height: 380px;
    background: linear-gradient(90deg, rgba(231,231,234,0) 0%, #c9cfd8 30%, var(--hull-blue) 70%, #4f6f9c 100%);
    border-radius: 0 0 40px 40px;
  }
  .boat-mark {
    position: absolute; left: 204px; top: 450px; width: 336px;
    transform: rotate(-90deg); transform-origin: 0 0;
    white-space: nowrap; color: var(--steel);
  }
  .boat-mark .boat-name {
    display: block; font-weight: 700; font-size: 50px; line-height: 42px; letter-spacing: 1px;
  }
  .boat-mark .boat-caption {
    display: flex; justify-content: space-between; align-items: center;
    padding-left: 12px; padding-right: 282px; position: relative;
    font-size: 12.5px; line-height: 18px;
  }
  .boat-mark .boat-home { font-weight: 500; }
  .boat-mark .boat-model {
    position: absolute; right: 14px; top: 0;
    font-weight: 600; font-size: 14px; letter-spacing: 1px;
  }
</style>
</head>
<body>
  <section class="card card-front">
    <div class="yacht-art" role="img" aria-label="Illustration of the company's motor yacht"></div>
    <div class="brand-name">POLAR TIDE</div>
    <h1 class="person-name">JOHNATHAN<br>DOE</h1>
    <div class="rule rule-top"></div>
    <p class="job-title">ACCOUNT MANAGER</p>
    <div class="contact-icons">
      <svg viewBox="0 0 25 25" aria-label="Phone">
        <rect width="25" height="25" rx="4" fill="var(--bronze)"/>
        <path d="M8 6.5c1-.8 1.8-.6 2.2.2l1 2c.3.6.1 1.2-.4 1.6l-.8.6c.7 1.6 1.8 2.8 3.4 3.6l.6-.8c.4-.5 1-.7 1.6-.4l2 1c.8.4 1 1.2.2 2.2-1 1.2-2.4 1.3-4 .5-2.8-1.4-5-3.6-6.3-6.4-.7-1.6-.6-3 .5-4.1z" fill="#fff"/>
      </svg>
      <svg viewBox="0 0 25 25" aria-label="Email">
        <rect width="25" height="25" rx="4" fill="var(--bronze)"/>
        <rect x="5.5" y="7.5" width="14" height="10" rx="1" fill="#fff"/>
        <path d="M5.8 8l6.7 5 6.7-5" fill="none" stroke="var(--bronze)" stroke-width="1.2"/>
      </svg>
      <svg viewBox="0 0 25 25" aria-label="Website">
        <rect width="25" height="25" rx="4" fill="var(--bronze)"/>
        <g fill="none" stroke="#fff" stroke-width="1.2">
          <circle cx="12.5" cy="12.5" r="6.5"/>
          <ellipse cx="12.5" cy="12.5" rx="3" ry="6.5"/>
          <path d="M6 12.5h13M7 9h11M7 16h11"/>
        </g>
      </svg>
    </div>
    <div class="rule rule-bottom"></div>
    <ul class="contact-list">
      <li>123 456 7890</li>
      <li>EMAIL@DOMAIN.COM</li>
      <li>WWW.WEBSITE.COM</li>
    </ul>
  </section>

  <section class="card card-back">
    <div class="boat-art" role="img" aria-label="Side-view line drawing of the center-console fishing boat"></div>
    <div class="boat-mark">
      <span class="boat-name">sea ember</span>
      <span class="boat-caption">
        <span class="boat-home">port arden, bay</span>
        <span class="boat-model">38SX</span>
      </span>
    </div>
  </section>
</body>
</html>
```